Lindenhof Köln, Greta Wommer sucht Design
Zielgruppe
Ich mache:
1. (lebendige) Stadtführungen bzw. Gästeführung in jeder Hinsicht -> in Köln für kleine und große Gruppen und vielfältige, individuelle Themen (bei größeren Gruppen setze ich zusätzliche Guides ein, so dass ich Veranstaltungen bis 300 Personen managen kann)
2. VIP-Gästebetreuung
3. 'Rundum-Sorglos-Pakete' = komplette Eventplanung und -durchführung, d. h. Programmerstellung nach Anzahl Teilnehmer, Budget und Zeitrahmen, einschließlich Auswahl Restaurants etc. und ggfls. Bereitstellung von Limousinen, Bussen oder anderen Fahrzeugen
4. Stadtrundfahrten (dazu biete ich Fahrzeuge unterschiedlicher Größe an, oder steige als Tour-Guide in den vorhandenen Bus einer Gruppe für die Stadtrundfahrt zu)
5. Schiffstouren
6. Komplett-Planung und Durchführung von Rahmen- oder Partnerprogrammen für Firmen, deren Kunden, Mitarbeiter oder Gäste am Rande einer Tagung, Konferenz etc. unterhalten werden sollen (z. B. eine Stadtführung nach der Konferenz und vor dem Abendessen)
7. Auch Halbtages- oder Ganztagesprogramme
Zielgruppe:
Ich arbeite zwar sehr viel für private Gruppe, die möchte ich unbedingt weiterhin ansprechen, aber zunehmend auch Firmen, da ich im Bereich der VIP-Gästebetreuung und 'Rundum-Sorglos-Planung' auf zahlreiche, sehr namhafte Referenzen verweisen kann.
a) Private Gruppen (für herkömmliche Stadtführung, -rundfahrt, Schiffstour im Rahmen von diversen Anlässen)
b) Firmen (für Kundenveranstaltungen, Firmenfeiern, Rahmenprogramm während Konferenz etc., Partnerprogramm (d. h. während die Konferenzteilnehmer tagen, kümmere ich mich um die mitgereisten Partner)
c) große namhafte Hotels, die ihren Gästen eine Gästeführerin vermitteln möchten
Aufgabenstellung
Ich wünsche mir, dass aus dem Logo hervorgeht, dass ich (zertifizierte) Stadtführerin (=Gästeführerin) in Köln bin und lege Wert darauf, dass mein Design vor allem Kompetenz, Professionalität, Innovation und Vertrauen ausstrahlt.
Bei Stadtführern in Köln findet sich im Logo meist der Kölner Dom (wie bei mir aktuell auch) oder das Stadtwappen Kölns, das schwarz-weiß-rot ist. Das Stadtwappen möchte ich auf KEINEN Fall, der Dom ist immer gut aber nicht zwingend.
Auf meiner Website www.lindenhof-koeln.de habe ich mit den Farben schwarz, weinrot und grau gearbeitet. Das gefällt mir noch immer, ist aber nicht in Stein gemeißelt. Ich bevorzuge auf jeden Fall KLARE Farben und ein KLARES Design. Eher minimalistisch als verschnörkelt.

```html
<!DOCTYPE html>
<html lang="de">
<head>
<meta charset="utf-8">
<title>Lindenhof Köln – Geschäftsausstattung</title>
<link href="https://fonts.googleapis.com/css2?family=Arimo:wght@400;700&display=swap" rel="stylesheet">
<style>
  :root {
    --brand-red: #e8262b;
    --ink: #1a1a1a;
    --paper: #ffffff;
    --edge: #d4d4d4;
    --backdrop: #ffffff;
    --signature: #d6ecf8;
  }
  * { margin: 0; padding: 0; box-sizing: border-box; }
  html, body { width: 1200px; height: 960px; overflow: hidden; background: var(--backdrop); }
  body { position: relative; font-family: "Arimo", Arial, sans-serif; color: var(--ink); }

  .sheet {
    position: absolute; background: var(--paper);
    border: 3px solid var(--edge);
    box-shadow: 6px 8px 14px rgba(0,0,0,0.18);
  }
  .letter { left: 46px; top: 35px; width: 624px; height: 883px; }
  .card { width: 407px; height: 266px; }
  .card-front { left: 734px; top: 35px; }
  .card-back { left: 734px; top: 356px; }

  .abs { position: absolute; }

  /* Wortmarke */
  .mark { position: absolute; text-align: center; }
  .mark .dot { display: block; margin: 0 auto; border-radius: 50%; background: var(--brand-red); }
  .mark .name { display: block; font-weight: 700; color: var(--brand-red); line-height: 1; }
  .mark .claim { display: block; line-height: 1.1; white-space: nowrap; }

  .letter .mark { left: 462px; top: 78px; width: 70px; }
  .letter .mark .dot { width: 66px; height: 66px; }
  .letter .mark .name { font-size: 13px; margin-top: 5px; }
  .letter .mark .claim { font-size: 6px; margin-top: 1px; }

  .card-front .mark { left: 123px; top: 42px; width: 155px; }
  .card-front .mark .dot { width: 142px; height: 142px; }
  .card-front .mark .name { font-size: 28px; margin-top: 14px; }
  .card-front .mark .claim { font-size: 14px; margin-top: 2px; }

  .card-back .mark { left: 33px; top: 35px; width: 80px; }
  .card-back .mark .dot { width: 76px; height: 76px; }
  .card-back .mark .name { font-size: 15px; margin-top: 7px; }
  .card-back .mark .claim { font-size: 7px; margin-top: 1px; }

  /* Brief */
  .sender-line { left: 60px; top: 148px; font-size: 9.5px; word-spacing: 2px; }
  .sender-line span + span { margin-left: 6px; }
  .recipient { left: 60px; top: 171px; font-size: 12.5px; line-height: 15px; }
  .info { left: 462px; font-size: 8px; line-height: 10px; }
  .info b { font-weight: 700; }
  .info-person { top: 172px; }
  .info-address { top: 216px; }
  .info-date { top: 329px; }
  .info-page { top: 822px; }
  .salutation { left: 60px; top: 330px; font-size: 12.5px; }
  .body-copy { left: 60px; top: 393px; width: 408px; font-size: 12.5px; line-height: 15px; }
  .signature { left: 60px; top: 596px; width: 76px; height: 30px; background: var(--signature); border-radius: 4px; }
  .closing { left: 60px; top: 645px; font-size: 12.5px; }

  .fold-mark { left: 0; width: 12px; height: 1px; background: var(--brand-red); }
  .fold-top { top: 318px; }
  .fold-bottom { top: 558px; }
  .punch-mark { left: 7px; top: 436px; }

  /* Visitenkarte Rückseite */
  .card-block { top: 158px; font-size: 13.5px; line-height: 16px; white-space: nowrap; }
  .card-person { left: 33px; }
  .card-contact { left: 212px; }
  .card-block b { font-weight: 700; }
</style>
</head>
<body>

<section class="sheet letter">
  <div class="mark">
    <span class="dot"></span>
    <span class="name">Lindenhof</span>
    <span class="claim">Greta Wommer führt in Köln</span>
  </div>

  <p class="abs sender-line"><span>Greta Wommer</span><span>Ulmenweg 12</span><span>50668 Köln</span></p>
  <p class="abs recipient">Firma<br>Max Mustermann<br>Beispielstraße 23a<br>12345 Berlin</p>

  <p class="abs info info-person"><b>Greta Wommer</b><br>Zertifizierte Gästeführerin<br>DIN EN 155</p>
  <p class="abs info info-address"><b>Adresse</b><br>Ulmenweg 12<br>50668 Köln</p>
  <p class="abs info info-date"><b>Datum</b><br>12 Mai 2017</p>

  <span class="abs fold-mark fold-top"></span>
  <span class="abs fold-mark fold-bottom"></span>
  <svg class="abs punch-mark" width="6" height="10" viewBox="0 0 6 10"><polygon points="0,0 6,5 0,10" fill="var(--brand-red)"/></svg>

  <p class="abs salutation">Sehr geehrter Herr Mustermann,</p>
  <p class="abs body-copy">Lorem ipsum dolor sit amet, consetetur sadipscing elitr, sed diam nonumy eirmod tempor invidunt ut labore et dolore magna aliquyam erat, sed diam voluptua. At vero eos et accusam et justo duo dolores et ea rebum. Stet clita kasd gubergren, no sea takimata sanctus est Lorem ipsum dolor sit amet. Lorem ipsum dolor sit amet, consetetur sadipscing elitr, sed diam nonumy eirmod tempor invidunt ut labore et dolore magna aliquyam erat, sed diam voluptua. At vero eos et accusam et justo duo dolores et ea rebum. Stet clita kasd gubergren, no sea takimata sanctus est Lorem ipsum dolor sit amet.</p>

  <div class="abs signature" role="img" aria-label="Handschriftliche Unterschrift"></div>
  <p class="abs closing">Mit freundlichen Grüßen</p>

  <p class="abs info info-page"><b>Seite</b><br>1 von 1</p>
</section>

<section class="sheet card card-front">
  <div class="mark">
    <span class="dot"></span>
    <span class="name">Lindenhof</span>
    <span class="claim">Greta Wommer führt in Köln</span>
  </div>
</section>

<section class="sheet card card-back">
  <div class="mark">
    <span class="dot"></span>
    <span class="name">Lindenhof</span>
    <span class="claim">Greta Wommer führt in Köln</span>
  </div>
  <p class="abs card-block card-person"><b>Greta Wommer</b><br>Zertifizierte Gästeführerin<br>DIN EN 155</p>
  <p class="abs card-block card-contact"><b>Kontakt:</b><br>Ulmenweg 12<br>50668 Köln<br>0171 23 45 678<br>kontakt@lindenhof-koeln.de</p>
</section>

</body>
</html>
```